Studying Effectively To Do List

I am looking to design a new "Study To Do List" for High School students (Ages 15 - 18) . This will be printed as an A4 notepad and so should only be a single A4 page.

The Design will need to be professional and look semi-serious but also be appealing to High school students (Ages 15 - 18) and should NOT be gender specific.

I have attached a word document outlining the structure of the page. The space provided should be large enough that people can write in it comfortably.

The notepad will most likely be printed in black and white but I'm also looking at coloured options - colours should be kept to a minimum.

This will be printed professionally and should also include a 3mm bleed.

The design should also include the business logo (included in the word document)

Target Market(s)

High School students (Ages 15 - 18). Both genders

Industry/Entity Type

Education

Font styles to use
Serif
Sans Serif

Requirements
Must have
• Please see the word document attached.
Should not have
• Too much colour

```html
<!DOCTYPE html>
<html lang="en">
<head>
<meta charset="utf-8">
<title>Study To Do List – Notepad Pages</title>
<link rel="stylesheet" href="https://fonts.googleapis.com/css2?family=Source+Sans+3:ital,wght@0,400;0,600;1,600&display=swap">
<style>
  :root {
    --paper: #ffffff;
    --ink: #1d1d1b;
    --bar: #d4d4d6;
    --rule: #5a5a5a;
    --teal: #157f9c;
    --green: #bcd86f;
    --black: #111111;
    --grey: #a7a7aa;
  }
  * { box-sizing: border-box; margin: 0; padding: 0; }
  html, body { width: 1200px; height: 880px; overflow: hidden; background: var(--paper); }
  body { position: relative; font-family: "Source Sans 3", "Myriad Pro", Arial, sans-serif; color: var(--ink); }

  .page { position: absolute; top: 32px; width: 570px; height: 814px; }
  .page--colour { left: 24px; --edge-a: var(--teal); --edge-b: var(--green); }
  .page--mono { left: 610px; --edge-a: var(--black); --edge-b: var(--grey); }

  .edge { position: absolute; }
  .edge--top { left: 0; top: 0; width: 570px; height: 13px; background: linear-gradient(90deg, var(--edge-a), var(--edge-b)); }
  .edge--left { left: 0; top: 0; width: 13px; height: 814px; background: var(--edge-a); }
  .edge--right { left: 557px; top: 0; width: 13px; height: 736px; background: var(--edge-b);
    clip-path: polygon(0 0, 100% 0, 100% 100%, 0 calc(100% - 7px)); }
  .edge--bottom { left: 0; top: 803px; width: 490px; height: 11px;
    background: linear-gradient(90deg, var(--edge-a), var(--edge-b));
    clip-path: polygon(0 0, 100% 0, calc(100% - 8px) 100%, 0 100%); }

  .heading { position: absolute; left: 44px; font-size: 11.5px; letter-spacing: .2px; text-transform: uppercase; }
  .heading--accent { font-weight: 600; font-style: italic; }

  .date { position: absolute; left: 404px; top: 30px; font-size: 11px; display: flex; align-items: flex-end; }
  .date .fill { width: 108px; border-bottom: 1px dotted var(--rule); margin: 0 0 3px 3px; }

  .bars { position: absolute; display: grid; gap: 4px 10px; }
  .bars--revision { left: 44px; top: 55px; grid-template-columns: 238px 238px; grid-auto-flow: column; grid-template-rows: repeat(4, 10px); }
  .bar { background: var(--bar); font-size: 7px; line-height: 10px; padding-left: 5px; }

  .rows { position: absolute; left: 44px; }
  .rows--homework { top: 142px; width: 486px; }
  .rows--assess { top: 433px; width: 501px; }
  .row { display: flex; align-items: flex-end; font-size: 11px; }
  .rows--homework .row { height: 20.7px; }
  .rows--assess .row { height: 21.5px; }
  .row .label { width: 76px; }
  .row .line { flex: 1; position: relative; border-bottom: 1px dotted var(--rule); margin-bottom: 4px; height: 1px; }
  .row .due { position: absolute; left: 189px; bottom: 0; font-size: 7px; background: var(--paper); padding-right: 1px; line-height: 8px; }

  .notes { position: absolute; left: 36px; top: 716px; width: 448px; height: 78px; border: 1.2px solid var(--ink); display: flex; }
  .notes__col { padding: 3px 5px; }
  .notes__col--notes { width: 230px; border-right: 1.2px solid var(--ink); }
  .notes__col--practice { flex: 1; }
  .notes__title { font-size: 11px; font-weight: 600; font-style: italic; text-transform: uppercase; height: 15px; }
  .notes__col--practice .notes__title { text-align: center; }
  .notes .bars { position: static; grid-template-rows: repeat(4, 10px); gap: 4px 4px; grid-auto-flow: column; }
  .notes__col--notes .bars { grid-template-columns: 106px 106px; }
  .notes__col--practice .bars { grid-template-columns: 1fr; }

  .brand { position: absolute; left: 490px; top: 740px; width: 76px; display: flex; flex-direction: column; align-items: center; gap: 4px; }
  .brand__dot { width: 34px; height: 34px; border-radius: 50%; background: var(--edge-a); }
  .brand__name { font-size: 12px; font-weight: 600; color: var(--ink); }
</style>
</head>
<body>

<!-- Colour version -->
<section class="page page--colour">
  <div class="edge edge--top"></div><div class="edge edge--left"></div><div class="edge edge--right"></div><div class="edge edge--bottom"></div>

  <h2 class="heading heading--accent" style="top:40px">Revision</h2>
  <p class="date">Date:<span class="fill"></span></p>
  <div class="bars bars--revision">
    <span class="bar">1</span><span class="bar">2</span><span class="bar">3</span><span class="bar">4</span>
    <span class="bar">5</span><span class="bar">6</span><span class="bar">7</span><span class="bar">8</span>
  </div>

  <h2 class="heading" style="top:132px">Homework</h2>
  <div class="rows rows--homework">
    <div class="row"><span class="label">Subject:</span><span class="line"></span></div>
    <div class="row"><span class="label">Task:</span><span class="line"></span></div>
    <div class="row"><span class="label">Subject:</span><span class="line"></span></div>
    <div class="row"><span class="label">Task:</span><span class="line"></span></div>
    <div class="row"><span class="label">Subject:</span><span class="line"></span></div>
    <div class="row"><span class="label">Task:</span><span class="line"></span></div>
    <div class="row"><span class="label">Subject:</span><span class="line"></span></div>
    <div class="row"><span class="label">Task:</span><span class="line"></span></div>
    <div class="row"><span class="label">Subject:</span><span class="line"></span></div>
    <div class="row"><span class="label">Task:</span><span class="line"></span></div>
    <div class="row"><span class="label">Subject:</span><span class="line"></span></div>
    <div class="row"><span class="label">Task:</span><span class="line"></span></div>
  </div>

  <h2 class="heading" style="top:421px">Assessments</h2>
  <div class="rows rows--assess">
    <div class="row"><span class="label">Assessment:</span><span class="line"><span class="due">Due</span></span></div>
    <div class="row"><span class="label">Element:</span><span class="line"><span class="due">Due</span></span></div>
    <div class="row"><span class="label">Assessment:</span><span class="line"><span class="due">Due</span></span></div>
    <div class="row"><span class="label">Element:</span><span class="line"><span class="due">Due</span></span></div>
    <div class="row"><span class="label">Assessment:</span><span class="line"><span class="due">Due</span></span></div>
    <div class="row"><span class="label">Element:</span><span class="line"><span class="due">Due</span></span></div>
    <div class="row"><span class="label">Assessment:</span><span class="line"><span class="due">Due</span></span></div>
    <div class="row"><span class="label">Element:</span><span class="line"><span class="due">Due</span></span></div>
    <div class="row"><span class="label">Assessment:</span><span class="line"><span class="due">Due</span></span></div>
    <div class="row"><span class="label">Element:</span><span class="line"></span></div>
    <div class="row"><span class="label">Assessment:</span><span class="line"><span class="due">Due</span></span></div>
    <div class="row"><span class="label">Element:</span><span class="line"><span class="due">Due</span></span></div>
  </div>

  <div class="notes">
    <div class="notes__col notes__col--notes">
      <p class="notes__title">Notes</p>
      <div class="bars"><span class="bar">1</span><span class="bar">2</span><span class="bar">3</span><span class="bar">4</span><span class="bar">5</span><span class="bar">6</span><span class="bar">7</span><span class="bar">8</span></div>
    </div>
    <div class="notes__col notes__col--practice">
      <p class="notes__title">Practice</p>
      <div class="bars"><span class="bar"></span><span class="bar"></span><span class="bar"></span><span class="bar"></span></div>
    </div>
  </div>

  <div class="brand"><span class="brand__dot"></span><span class="brand__name">Northvale</span></div>
</section>

<!-- Black and white version -->
<section class="page page--mono">
  <div class="edge edge--top"></div><div class="edge edge--left"></div><div class="edge edge--right"></div><div class="edge edge--bottom"></div>

  <h2 class="heading heading--accent" style="top:40px">Revision</h2>
  <p class="date">Date:<span class="fill"></span></p>
  <div class="bars bars--revision">
    <span class="bar">1</span><span class="bar">2</span><span class="bar">3</span><span class="bar">4</span>
    <span class="bar">5</span><span class="bar">6</span><span class="bar">7</span><span class="bar">8</span>
  </div>

  <h2 class="heading" style="top:132px">Homework</h2>
  <div class="rows rows--homework">
    <div class="row"><span class="label">Subject:</span><span class="line"></span></div>
    <div class="row"><span class="label">Task:</span><span class="line"></span></div>
    <div class="row"><span class="label">Subject:</span><span class="line"></span></div>
    <div class="row"><span class="label">Task:</span><span class="line"></span></div>
    <div class="row"><span class="label">Subject:</span><span class="line"></span></div>
    <div class="row"><span class="label">Task:</span><span class="line"></span></div>
    <div class="row"><span class="label">Subject:</span><span class="line"></span></div>
    <div class="row"><span class="label">Task:</span><span class="line"></span></div>
    <div class="row"><span class="label">Subject:</span><span class="line"></span></div>
    <div class="row"><span class="label">Task:</span><span class="line"></span></div>
    <div class="row"><span class="label">Subject:</span><span class="line"></span></div>
    <div class="row"><span class="label">Task:</span><span class="line"></span></div>
  </div>

  <h2 class="heading" style="top:421px">Assessments</h2>
  <div class="rows rows--assess">
    <div class="row"><span class="label">Assessment:</span><span class="line"><span class="due">Due</span></span></div>
    <div class="row"><span class="label">Element:</span><span class="line"><span class="due">Due</span></span></div>
    <div class="row"><span class="label">Assessment:</span><span class="line"><span class="due">Due</span></span></div>
    <div class="row"><span class="label">Element:</span><span class="line"><span class="due">Due</span></span></div>
    <div class="row"><span class="label">Assessment:</span><span class="line"><span class="due">Due</span></span></div>
    <div class="row"><span class="label">Element:</span><span class="line"><span class="due">Due</span></span></div>
    <div class="row"><span class="label">Assessment:</span><span class="line"><span class="due">Due</span></span></div>
    <div class="row"><span class="label">Element:</span><span class="line"><span class="due">Due</span></span></div>
    <div class="row"><span class="label">Assessment:</span><span class="line"><span class="due">Due</span></span></div>
    <div class="row"><span class="label">Element:</span><span class="line"></span></div>
    <div class="row"><span class="label">Assessment:</span><span class="line"><span class="due">Due</span></span></div>
    <div class="row"><span class="label">Element:</span><span class="line"><span class="due">Due</span></span></div>
  </div>

  <div class="notes">
    <div class="notes__col notes__col--notes">
      <p class="notes__title">Notes</p>
      <div class="bars"><span class="bar">1</span><span class="bar">2</span><span class="bar">3</span><span class="bar">4</span><span class="bar">5</span><span class="bar">6</span><span class="bar">7</span><span class="bar">8</span></div>
    </div>
    <div class="notes__col notes__col--practice">
      <p class="notes__title">Practice</p>
      <div class="bars"><span class="bar"></span><span class="bar"></span><span class="bar"></span><span class="bar"></span></div>
    </div>
  </div>

  <div class="brand"><span class="brand__dot"></span><span class="brand__name">Northvale</span></div>
</section>

</body>
</html>
```